Willowbend Spine Chiropractic

office phone- 913-462-1037
After Hour number 913-284-6150
Office address 27814 Halvorn Rd. Overland Park Ks 66947
Dr. Marlon Pettigrew, DC
I added 3 different types of logos proofs.
Specalizing in:
Family Wellness Care
Auto Accident
Workman Comp Injuries
Urgent Alternative Pain Relief
Non-operative Sports Injury Care

```html
<!DOCTYPE html>
<html lang="en">
<head>
<meta charset="utf-8">
<title>Willowbend Spine Chiropractic – Business Card</title>
<link rel="stylesheet" href="https://fonts.googleapis.com/css2?family=Noto+Sans:wght@400;800&display=swap">
<style>
  :root {
    --page-bg: #e9eaec;
    --sky-light: #c9d2e3;
    --sky-mid: #97a5c2;
    --sky-deep: #6f7e9e;
    --sky-haze: #e4e9f2;
    --brand-navy: #262f8c;
    --ink: #111318;
    --ink-soft: #23262d;
    --card-edge: #2b3470;
  }
  * { box-sizing: border-box; margin: 0; padding: 0; }
  html, body {
    width: 1200px; height: 900px; overflow: hidden;
    background: var(--page-bg);
    font-family: "Noto Sans", "DejaVu Sans", Verdana, sans-serif;
  }
  .canvas {
    position: relative; width: 1200px; height: 900px;
  }
  .card {
    position: absolute; left: 250px; width: 700px; height: 400px;
    overflow: hidden;
    border-bottom: 3px solid var(--card-edge);
    box-shadow: 0 6px 18px rgba(0,0,0,.25);
  }
  .card--front { top: 36px; }
  .card--back { top: 464px; }
  .sky-backdrop {
    position: absolute; inset: 0;
    background:
      radial-gradient(ellipse 40% 35% at 30% 30%, var(--sky-haze), transparent 70%),
      radial-gradient(ellipse 35% 40% at 75% 65%, var(--sky-light), transparent 70%),
      radial-gradient(ellipse 30% 30% at 55% 80%, var(--sky-deep), transparent 75%),
      linear-gradient(160deg, var(--sky-mid), var(--sky-light) 45%, var(--sky-mid) 75%, var(--sky-deep));
  }
  .brand {
    position: absolute; inset: 0;
    display: flex; align-items: center; justify-content: center; gap: 22px;
    padding: 0 40px;
  }
  .brand__mark {
    flex: none; width: 26px; height: 26px; border-radius: 50%;
    background: var(--brand-navy);
  }
  .brand__name {
    font-weight: 800; font-size: 50px; line-height: 1.05;
    color: var(--brand-navy); text-transform: uppercase; letter-spacing: .5px;
  }
  .back-content {
    position: absolute; inset: 0; color: var(--ink);
  }
  .doctor-name {
    position: absolute; left: 34px; top: 28px;
    font-size: 27px; font-weight: 400;
  }
  .address {
    position: absolute; left: 34px; top: 86px;
    font-size: 23px; line-height: 1.25; font-style: normal;
  }
  .phones {
    position: absolute; left: 34px; top: 232px;
    font-size: 18px; line-height: 1.35; list-style: none;
  }
  .specialties {
    position: absolute; left: 338px; top: 176px;
    font-size: 18px; line-height: 1.32; color: var(--ink-soft);
  }
  .specialties__list { list-style: none; }
  .specialties__list li:first-child { padding-left: 28px; }
  .specialties__list li:nth-child(2),
  .specialties__list li:nth-child(3) { padding-left: 18px; }
</style>
</head>
<body>
<main class="canvas">
  <section class="card card--front" aria-label="Card front">
    <div class="sky-backdrop" role="img" aria-label="Soft cloudy blue-grey sky backdrop"></div>
    <div class="brand">
      <span class="brand__mark" aria-hidden="true"></span>
      <h1 class="brand__name">Willowbend Spine<br>Chiropractic</h1>
    </div>
  </section>

  <section class="card card--back" aria-label="Card back">
    <div class="sky-backdrop" role="img" aria-label="Soft cloudy blue-grey sky backdrop"></div>
    <div class="back-content">
      <h2 class="doctor-name">Dr. Marlon Pettigrew</h2>
      <address class="address">27814 Halvorn Rd,<br>Overland Park,<br>Ks 66947</address>
      <ul class="phones">
        <li>Office: 913-462-1037</li>
        <li>After office: 913-284-6150</li>
      </ul>
      <div class="specialties">
        <p>Specializing in:</p>
        <ul class="specialties__list">
          <li>Family wellness care</li>
          <li>Auto accident</li>
          <li>workman comp injuries</li>
          <li>Urgent alternative pain relief</li>
          <li>Non-operative sports injury care</li>
        </ul>
      </div>
    </div>
  </section>
</main>
</body>
</html>
```